Website for Painting Company

Hi,
We are after a Wordpress website design with CSS/HTML Theme for our painting company based in Brisbane, Australia. Our business name is Felix Morrow Painting Contractors and we have been trading for 33 years.
We want a website that is modern and fresh with a professional image. Our organisation does Commercial, Residential and Insurance Painting projects. I have listed a couple of similar websites that we like the look and feel of. These are a guide only and we are happy to see you own designs with a similar professional image.
http://www.kelbrookcoatings.com.au/
http://www.tidewellfinishes.com.au/
We are a member of Guild Decorators Australia and I have supplied the logo named "gda" which I have included in the files I have uploaded.
We want a five page site. These are Home Page, Residential, Commercial, Insurance and Contact Us.
I have also uploaded our logo and some pictures labeled Logo,Residential, Commercial, Insurance and Homepage. These should be used on each page listed above.
Updates
Project Deadline Extended
Reason: We are extending because we need more time to go through the designs and give feedback. There are many fantastic designs. Thank you everyone who has contributed!!!!
All the best
Derek
Industry/Entity Type
Painting
Requirements
Must have
- We want a five page site. These are Home Page, Residential, Commercial, Insurance and Contact Us.

```html
<!DOCTYPE html>
<html lang="en">
<head>
<meta charset="utf-8">
<title>Felix Morrow Painting Contractors</title>
<link rel="stylesheet" href="https://fonts.googleapis.com/css2?family=Arimo:wght@400;700&family=Gelasio:ital,wght@0,400;0,700;1,400;1,700&family=Oswald:wght@500&display=swap">
<style>
:root{
  --red:#c8141c;
  --ink:#333;
  --peach:#e6a884;
  --olive:#a9ad6a;
  --pink:#d98bb4;
  --blue:#9aabd4;
  --lavender:#a7b3e2;
  --orange:#f0a81e;
  --green:#3d9a2c;
  --sky:#3a8fc8;
  --beige:#f4efe2;
  --footer:#3b3b3b;
  --phone:#d28a5c;
}
*{margin:0;padding:0;box-sizing:border-box}
html,body{width:863px;height:1200px;overflow:hidden;background:#fff}
body{position:relative;font-family:"Arimo",Arial,sans-serif;color:var(--ink)}
.abs{position:absolute}
.swirl-top{left:560px;top:-40px;width:340px;height:560px;background:radial-gradient(ellipse at 70% 30%,rgba(240,90,30,.85),rgba(250,170,60,.45) 45%,rgba(255,255,255,0) 70%)}
.swirl-left{left:-120px;top:220px;width:560px;height:300px;background:radial-gradient(ellipse at 30% 50%,rgba(250,200,80,.55),rgba(250,170,60,.25) 45%,rgba(255,255,255,0) 70%)}
.waves{left:0;top:990px;width:863px;height:210px}
.brand{left:103px;top:38px;display:flex;align-items:center;gap:8px}
.brand-mark{width:22px;height:22px;background:var(--red)}
.brand-name{font-family:"Gelasio",Georgia,serif;font-weight:700;font-size:15px;color:var(--red);line-height:1.2;width:170px}
.call{left:635px;top:24px}
.call-label{font-size:17px;color:#2a2a2a}
.call-number{font-size:20px;color:var(--phone);margin-top:1px}
.nav{left:381px;top:100px;display:flex;height:25px}
.nav a{width:76px;text-align:center;color:#fff;font-family:"Gelasio",Georgia,serif;font-size:10px;line-height:25px;text-decoration:none;border-right:1px solid rgba(255,255,255,.6);white-space:nowrap}
.hero{left:101px;top:125px;width:660px;height:263px;background:linear-gradient(160deg,#f0d9a0 0%,#e8c277 35%,#c79353 65%,#8a5a30 100%)}
.services{left:104px;top:407px;width:506px;height:210px;background:#fff;box-shadow:0 0 4px rgba(0,0,0,.25);display:flex}
.service{width:168.6px;border-right:1px solid #e5e5e5;position:relative}
.service:last-child{border-right:0}
.service-head{height:65px;background:linear-gradient(#fff,#ececec);display:flex;align-items:center;padding-left:8px;gap:10px}
.service-icon{width:44px;height:44px;border-radius:6px}
.service-title{font-size:14px;line-height:14px;color:#222}
.service-body{font-size:8.8px;line-height:13.5px;color:#333;padding:14px 8px 0 14px;letter-spacing:-.1px}
.read-more{position:absolute;left:14px;top:179px;background:#e3e3e3;border-radius:3px;font-size:9px;padding:4px 6px;color:#222}
.quote{left:606px;top:422px;width:130px;height:180px}
.welcome{left:110px;top:645px;width:496px}
.welcome h1{font-family:"Gelasio",Georgia,serif;font-weight:400;font-size:19px;line-height:21px;color:#444}
.welcome h1 span{display:block;color:var(--red)}
.welcome p{font-size:9.3px;line-height:17px;color:#333;margin-top:6px}
.members{left:627px;top:643px;width:134px;height:155px;background:#fff;box-shadow:0 0 4px rgba(0,0,0,.25);text-align:center}
.members h2{font-family:"Gelasio",Georgia,serif;font-weight:400;font-size:18px;color:var(--sky);margin-top:5px}
.members-sub{font-size:8.5px;font-weight:700;font-style:italic;color:#1f3f9a;margin-top:6px}
.members-badge{width:100px;height:70px;margin:8px auto 0;background:linear-gradient(135deg,#2b4aa8,#e3453c)}
.testimonials{left:101px;top:857px;width:512px;height:111px;background:var(--beige)}
.testimonials h2{position:absolute;left:0;right:0;top:8px;text-align:center;font-weight:400;font-size:15.5px;color:#222}
.testimonials hr{position:absolute;left:16px;right:16px;top:33px;border:0;border-top:1px solid #ddd4bf}
.quote-mark{position:absolute;font-family:"Gelasio",Georgia,serif;font-size:60px;color:#d9ceb3;line-height:1}
.testimonial{position:absolute;top:43px;width:232px;font-family:"Gelasio",Georgia,serif;font-style:italic;font-size:8.7px;line-height:14.5px;color:#333;letter-spacing:-.1px}
.testimonial b{display:block;font-family:"Arimo",Arial,sans-serif;font-style:normal;font-weight:400;font-size:9.2px;color:#111;margin-top:1px}
.seal{left:638px;top:843px;width:119px;height:119px;border-radius:50%;background:radial-gradient(circle,#e62a1c 0,#b0100c 60%,#c99a2a 61%,#b0100c 68%)}
.footer{left:101px;top:1012px;width:660px;height:167px;background:var(--footer);border-radius:6px 6px 0 0;color:#fff}
.fcol{position:absolute;top:24px}
.fcol h3{font-size:10px;font-weight:700;color:var(--orange);margin-bottom:6px}
.fcol li{list-style:none;font-size:8.6px;line-height:15.5px}
.fcol p{font-size:8.6px;line-height:13.5px}
.fcall{position:absolute;left:404px;top:22px}
.fcall-label{font-family:"Oswald",sans-serif;font-weight:500;font-size:19px;color:var(--orange)}
.fcall-number{font-family:"Gelasio",Georgia,serif;font-size:17px;color:#fff}
.social{display:flex;gap:6px;margin-top:4px}
.social span{width:20px;height:20px;border-radius:2px}
.copyright{position:absolute;left:27px;top:133px;font-size:8.4px}
</style>
</head>
<body>
<div class="abs swirl-top" role="img" aria-label="Orange paint swirl decoration"></div>
<div class="abs swirl-left" role="img" aria-label="Yellow paint swirl decoration"></div>
<svg class="abs waves" viewBox="0 0 863 210" aria-hidden="true">
  <path d="M0 60 C250 0 550 120 863 40" fill="none" stroke="#7cc9d6" stroke-width="2" opacity=".7"/>
  <path d="M0 80 C250 20 550 150 863 70" fill="none" stroke="#8ccf6a" stroke-width="3" opacity=".6"/>
  <path d="M0 120 C300 60 520 200 863 110 L863 210 L0 210Z" fill="#9fd37a" opacity=".35"/>
  <path d="M0 160 C300 110 520 210 863 150 L863 210 L0 210Z" fill="#5fb7c9" opacity=".3"/>
</svg>

<header>
  <div class="abs brand"><span class="brand-mark"></span><span class="brand-name">Felix Morrow and Co.<br>Painting Contractor</span></div>
  <div class="abs call"><div class="call-label">Call Now!</div><div class="call-number">(07) 3184 2260</div></div>
  <nav class="abs nav">
    <a href="#" style="background:var(--peach)">HOME</a>
    <a href="#" style="background:var(--olive)">RESIDENTIAL</a>
    <a href="#" style="background:var(--pink)">COMMERCIAL</a>
    <a href="#" style="background:var(--blue)">INSURANCE</a>
    <a href="#" style="background:var(--lavender)">CONTACT US</a>
  </nav>
</header>

<div class="abs hero" role="img" aria-label="Warmly lit living room with fireplace and armchairs"></div>

<section class="abs services">
  <div class="service">
    <div class="service-head"><span class="service-icon" role="img" aria-label="House icon" style="background:linear-gradient(#e0a040,#b52a1c)"></span><span class="service-title">Residential<br>Painting</span></div>
    <p class="service-body">Lorem ipsum dolor sit amet, consectetur adipisicing elit, sed do eiusmod tempor incididunt ut labore et dolore magna aliqua. Ut enim ad minim veniam, quis nostrud exercitation ullamco laboris nisi ut aliquip ex ea commodo consequat.</p>
    <span class="read-more">Read More</span>
  </div>
  <div class="service">
    <div class="service-head"><span class="service-icon" role="img" aria-label="Office building icon" style="background:linear-gradient(#cfd6dc,#5d6a76)"></span><span class="service-title">Commercial<br>Painting</span></div>
    <p class="service-body">Lorem ipsum dolor sit amet, consectetur adipisicing elit, sed do eiusmod tempor incididunt ut labore et dolore magna aliqua. Ut enim ad minim veniam, quis nostrud exercitation ullamco laboris nisi ut aliquip ex ea commodo consequat.</p>
    <span class="read-more">Read More</span>
  </div>
  <div class="service">
    <div class="service-head"><span class="service-icon" role="img" aria-label="Paint tin icon" style="background:linear-gradient(#e3e6e8,#7c8a92)"></span><span class="service-title">Insurance<br>Painting</span></div>
    <p class="service-body">Lorem ipsum dolor sit amet, consectetur adipisicing elit, sed do eiusmod tempor incididunt ut labore et dolore magna aliqua. Ut enim ad minim veniam, quis nostrud exercitation ullamco laboris nisi ut aliquip ex ea commodo consequat.</p>
    <span class="read-more">Read More</span>
  </div>
</section>

<svg class="abs quote" viewBox="0 0 130 180" role="img" aria-label="Get a Quote button with paint splash">
  <defs><linearGradient id="splash" x1="0" y1="0" x2="0" y2="1"><stop offset="0" stop-color="#2f7ac8"/><stop offset=".6" stop-color="#3fb0a8"/><stop offset="1" stop-color="#7cc24a"/></linearGradient></defs>
  <circle cx="62" cy="90" r="66" fill="url(#splash)" opacity=".85"/>
  <circle cx="62" cy="90" r="57" fill="#fff" stroke="#ddd" stroke-width="2"/>
  <text x="16" y="86" font-family="Gelasio, Georgia, serif" font-style="italic" font-weight="700" font-size="20" fill="#3d9a2c">Get a</text>
  <text x="16" y="108" font-family="Gelasio, Georgia, serif" font-style="italic" font-weight="700" font-size="20" fill="#3d9a2c">Quote</text>
  <path d="M84 74 L98 92 L84 110" fill="none" stroke="#c8c8c8" stroke-width="4"/>
</svg>

<section class="abs welcome">
  <h1>Welcome to <span>Felix Morrow Painting Contractors</span></h1>
  <p>If you live near Perth or you have a commercial building in this part of Australia, then you will want to look for painters Perth who can do both residential as well as commercial painting. You do not have to search far and wide to get good painting Perth as you will be able to find what you are looking for right online. Most people today find the businesses that they are seeking for services such as painting when they go on the Internet. If you live near Perth or you have a commercial building in this part of Australia, then you will want to look for painters Perth who can do both residential as well as commercial painting. You do not have to search far and wide to get good painting Perth as you will be able to find what you are looking for right online. Most people today find the businesses that they are seeking for services such as painting when they go on the Internet.</p>
</section>

<aside class="abs members">
  <h2>Memberships</h2>
  <div class="members-sub">Registered Member</div>
  <div class="members-badge" role="img" aria-label="Membership badge"></div>
</aside>

<section class="abs testimonials">
  <span class="quote-mark" style="left:10px;top:-14px">&ldquo;</span>
  <span class="quote-mark" style="left:472px;top:90px">&rdquo;</span>
  <h2>Testimonials</h2>
  <hr>
  <p class="testimonial" style="left:18px">"Thank you very much. I am 100% pleased with the work. They did a great, professional job. My thanks to the team for their good work and professionalism."<b>— Maren Holloway</b></p>
  <p class="testimonial" style="left:270px">"Thank you very much. I am 100% pleased with the work. They did a great, professional job. My thanks to the team for their good work and professionalism."<b>— Maren Holloway</b></p>
</section>

<div class="abs seal" role="img" aria-label="Quality guarantee seal"></div>

<footer class="abs footer">
  <div class="fcol" style="left:27px"><h3>QUICK LINKS</h3><ul><li>Home</li><li>Residential</li><li>Commercial</li><li>Insurance</li><li>Contact Us</li></ul></div>
  <div class="fcol" style="left:139px"><h3>OUR LOCATION</h3><p># 40, Lorem ipsum<br>1st Main, Dolor sit Amet<br>Lorem ipsum</p></div>
  <div class="fcol" style="left:270px"><h3>EMAIL</h3><p>info@felixmorrow.com</p></div>
  <div class="fcall"><div class="fcall-label">CALL NOW!</div><div class="fcall-number">(07) 3184 2260</div></div>
  <div class="fcol" style="left:559px"><h3>FOLLOW US</h3><div class="social"><span style="background:#3b5b9a"></span><span style="background:#3fb0dc"></span><span style="background:#1f78b4"></span></div></div>
  <p class="copyright">© 2011 Felix Morrow Painting Contractors. All rights reserved.</p>
</footer>
</body>
</html>
```